Business card design needed

We need something on the back that allows the customer to get five stamps then the sixth visit they get 25 dollars to spend.
Industry/Entity Type
Business
Contact Information for Business Card
Quality meat,value for money,spit roast hire, wholesale pubs clubs,cater for bbqs.marlow lane butchery 217 marlow lane.64739204.

```html
<!DOCTYPE html>
<html lang="en">
<head>
<meta charset="utf-8">
<title>Marlow Lane Butchery – Business Cards</title>
<link href="https://fonts.googleapis.com/css2?family=Jost:wght@400&family=Cinzel:wght@400&display=swap" rel="stylesheet">
<style>
  :root {
    --backdrop: #e6e6e6;
    --card: #ffffff;
    --ink: #3a3a3a;
    --ink-soft: #555555;
    --stamp: #8e8e8e;
    --stamp-text: #2f2f2f;
  }
  * { margin: 0; padding: 0; box-sizing: border-box; }
  html, body { width: 1200px; height: 1000px; overflow: hidden; }
  body {
    background: var(--backdrop);
    position: relative;
    font-family: "Jost", sans-serif;
    color: var(--ink);
  }
  .card {
    position: absolute;
    width: 390px;
    height: 224px;
    background: var(--card);
    box-shadow: 0 2px 10px rgba(0,0,0,0.12);
  }
  .card--front-a { left: 150px; top: 250px; }
  .card--front-b { left: 660px; top: 250px; }
  .card--loyalty { left: 405px; top: 600px; }

  .brand-wordmark {
    position: absolute;
    top: 62px; left: 0; right: 0;
    text-align: center;
    font-size: 22px;
    letter-spacing: 1px;
    color: var(--ink);
  }
  .brand-seal {
    position: absolute;
    left: 130px; top: 22px;
    width: 130px; height: 130px;
    border: 1px solid var(--ink);
    border-radius: 50%;
    display: flex; align-items: center; justify-content: center;
    text-align: center;
    font-family: "Cinzel", serif;
    font-size: 14px;
    line-height: 1.35;
    letter-spacing: 2px;
    color: var(--ink);
  }
  .contact {
    position: absolute;
    bottom: 26px;
    display: flex;
    gap: 8px;
    font-size: 10.5px;
    line-height: 1.3;
    color: var(--ink-soft);
  }
  .contact--address { left: 26px; }
  .contact--phone { left: 198px; }
  .contact svg { width: 12px; height: 14px; flex: none; margin-top: 2px; fill: var(--ink); }

  .stamp-row {
    position: absolute;
    left: 20px; right: 20px;
    display: flex;
    justify-content: space-between;
  }
  .stamp-row--top { top: 26px; }
  .stamp-row--bottom { top: 140px; }
  .stamp {
    width: 46px; height: 46px;
    border-radius: 50%;
    background: var(--stamp);
  }
  .stamp--reward {
    display: flex; align-items: center; justify-content: center;
    text-align: center;
    font-family: "Cinzel", serif;
    font-size: 11px;
    line-height: 1.05;
    letter-spacing: 1px;
    color: var(--stamp-text);
  }
  .loyalty-offer {
    position: absolute;
    top: 86px; left: 0; right: 0;
    text-align: center;
    font-family: "Cinzel", serif;
    font-size: 14px;
    line-height: 1.25;
    color: var(--stamp-text);
  }
</style>
</head>
<body>

<section class="card card--front-a">
  <div class="brand-wordmark">marlow lane butchery</div>
  <div class="contact contact--address">
    <svg viewBox="0 0 12 14" aria-hidden="true"><path d="M6 0a5 5 0 0 0-5 5c0 3.5 5 9 5 9s5-5.5 5-9a5 5 0 0 0-5-5zm0 7a2 2 0 1 1 0-4 2 2 0 0 1 0 4z"/></svg>
    <div>217 Marlow Lane<br>Eastbrook NSW 2841</div>
  </div>
  <div class="contact contact--phone">
    <svg viewBox="0 0 12 14" aria-hidden="true"><path d="M2.5 1l2 0 1 3-1.3 1.2c.7 1.6 1.9 2.9 3.4 3.6L8.8 7.5l3 1v2.2c0 .6-.5 1.3-1.3 1.3C5.2 12 1 7.8 1 2.5 1 1.7 1.7 1 2.5 1z"/></svg>
    <div>02 6473 9204<br>marlowlanebutchery@mailpost.com</div>
  </div>
</section>

<section class="card card--front-b">
  <div class="brand-seal">Marlow Lane<br>Butchery</div>
  <div class="contact contact--address">
    <svg viewBox="0 0 12 14" aria-hidden="true"><path d="M6 0a5 5 0 0 0-5 5c0 3.5 5 9 5 9s5-5.5 5-9a5 5 0 0 0-5-5zm0 7a2 2 0 1 1 0-4 2 2 0 0 1 0 4z"/></svg>
    <div>217 Marlow Lane<br>Eastbrook NSW 2841</div>
  </div>
  <div class="contact contact--phone">
    <svg viewBox="0 0 12 14" aria-hidden="true"><path d="M2.5 1l2 0 1 3-1.3 1.2c.7 1.6 1.9 2.9 3.4 3.6L8.8 7.5l3 1v2.2c0 .6-.5 1.3-1.3 1.3C5.2 12 1 7.8 1 2.5 1 1.7 1.7 1 2.5 1z"/></svg>
    <div>02 6473 9204<br>marlowlanebutchery@mailpost.com</div>
  </div>
</section>

<section class="card card--loyalty">
  <div class="stamp-row stamp-row--top">
    <div class="stamp" role="img" aria-label="Stamp space with cow silhouette"></div>
    <div class="stamp" role="img" aria-label="Stamp space with cow silhouette"></div>
    <div class="stamp" role="img" aria-label="Stamp space with cow silhouette"></div>
    <div class="stamp" role="img" aria-label="Stamp space with cow silhouette"></div>
    <div class="stamp" role="img" aria-label="Stamp space with cow silhouette"></div>
    <div class="stamp stamp--reward">$25<br>OFF</div>
  </div>
  <p class="loyalty-offer">Spend $50 on each visit and<br>receive $25 off your 6th visit!</p>
  <div class="stamp-row stamp-row--bottom">
    <div class="stamp" role="img" aria-label="Stamp space with cow silhouette"></div>
    <div class="stamp" role="img" aria-label="Stamp space with cow silhouette"></div>
    <div class="stamp" role="img" aria-label="Stamp space with cow silhouette"></div>
    <div class="stamp" role="img" aria-label="Stamp space with cow silhouette"></div>
    <div class="stamp" role="img" aria-label="Stamp space with cow silhouette"></div>
    <div class="stamp stamp--reward">$25<br>OFF</div>
  </div>
</section>

</body>
</html>
```